Dental FAQ/advert tri-fold for holistic family dentist

We are a dental clinic with a holistic emphasis. We are seeking new clients, mainly middle classed families. A tri-fold brochure that is both a useful dental FAQ to keep in the house and acts as an advertisement for our clinic. It will be mailed out. It needs to look clean, modern, somewhat minimalist, and I want it to follow the Zelvo design esthetic. website is oakmeadowsmileclinic.com
Updates

I just updated the pamphlet file with revised text! Thanks for the nice designs so far, keep em coming.

Target Market(s)

Young families. Upper middle classes.

Industry/Entity Type

Dental

Requirements
Must have
• Follows our logo and colours.

```html
<!DOCTYPE html>
<html lang="en">
<head>
<meta charset="UTF-8">
<title>Dental FAQ Brochure – Inside Panels</title>
<link rel="stylesheet" href="https://fonts.googleapis.com/css2?family=Questrial&display=swap">
<style>
  :root {
    --paper: #ffffff;
    --ink: #1d1d1f;
    --heading: #2a3588;
    --tile-light: #f1efee;
    --tile-warm: #e7c9b6;
    --tile-skin: #d9a88d;
    --tile-hair: #b88a5a;
    --tile-pink: #e6b7c0;
  }
  * { margin: 0; padding: 0; box-sizing: border-box; }
  html, body {
    width: 1200px; height: 849px; overflow: hidden;
    background: var(--paper);
  }
  .brochure {
    position: relative; width: 1200px; height: 849px;
    font-family: "Questrial", "Century Gothic", sans-serif;
    color: var(--ink);
  }
  .panel { position: absolute; top: 20px; }
  .panel--left { left: 22px; width: 378px; }
  .panel--middle { left: 412px; width: 385px; top: 22px; }
  .panel--right { left: 814px; width: 370px; }
  .faq-question {
    font-style: italic; font-weight: 400;
    font-size: 17px; line-height: 19.5px;
    color: var(--heading);
    margin-bottom: 12px;
    letter-spacing: 0.1px;
  }
  .faq-answer {
    font-size: 16px; line-height: 17.6px;
    margin-bottom: 13px;
    white-space: nowrap;
    letter-spacing: 0.1px;
  }
  .photo-grid {
    display: block;
    margin: 26px 0 38px 2px;
  }
</style>
</head>
<body>
<main class="brochure">

  <section class="panel panel--left">
    <h2 class="faq-question">When should my child first start visiting the<br>dentist?</h2>
    <p class="faq-answer">The Northland Dental Society<br>recommends bringing your children to visit<br>the dentist 6 months after their first tooth<br>has appeared. We recommend bringing<br>children in for short “happy visits” that build<br>their confidence and comfort in being at our<br>dental clinic. A happy visit is free unless dental<br>services are provided. Children can observe<br>your appointments and they can learn the<br>fun parts of the dental visit such as counting<br>and polishing teeth, and<br>riding up and down in the dental chair. And<br>of course, the best part, the prize drawer<br>at the end of the appointment! We find<br>that children who come for happy visits<br>experience little to no dental fear or anxiety in<br>their coming years.</p>

    <h2 class="faq-question">How often should I get dental checkups<br>and cleanings?</h2>
    <p class="faq-answer">Everybody is different, and has different needs<br>when it comes to regular examinations and<br>cleanings. Most people need to have their<br>teeth cleaned at least every 6 months. Those<br>with gum disease present may require more<br>frequent appointments.</p>

    <h2 class="faq-question">How do I know my dental office is clean?</h2>
    <p class="faq-answer">Dental offices in Alberta follow the most<br>stringent regulations in the world for<br>sterilization and infection control. The<br>operatory’s are cleaned between every<br>patient, staff members thoroughly wash their<br>hands regularly, and items are put through an<br>auto-clave system for sterilization. Our dental<br>staff members would be happy to show you<br>exactly how your safety is protected.</p>

    <h2 class="faq-question">Can I visit the dentist if I am pregnant?</h2>
    <p class="faq-answer">Regular dental cleanings are especially<br>important during pregnancy, as pregnancy</p>
  </section>

  <section class="panel panel--middle">
    <p class="faq-answer">gingivitis affects up to 50-70% of pregnant<br>women. Gum disease has been linked to<br>low birth weight and premature delivery. We<br>recommend a thorough dental exam and<br>cleaning if you are pregnant or planning on<br>having a baby.</p>

    <svg class="photo-grid" width="384" height="290" viewBox="0 0 384 290" role="img" aria-label="Photo of a mother and young daughter brushing their teeth together, shown as a grid of rounded tiles">
      <defs>
        <linearGradient id="photo-tone" x1="0" y1="0" x2="1" y2="0.4">
          <stop offset="0" stop-color="var(--tile-light)"/>
          <stop offset="0.22" stop-color="var(--tile-hair)"/>
          <stop offset="0.42" stop-color="var(--tile-skin)"/>
          <stop offset="0.62" stop-color="var(--tile-warm)"/>
          <stop offset="0.8" stop-color="var(--tile-light)"/>
          <stop offset="1" stop-color="#f7f7f7"/>
        </linearGradient>
        <linearGradient id="photo-shade" x1="0" y1="0" x2="0" y2="1">
          <stop offset="0" stop-color="#ffffff" stop-opacity="0.15"/>
          <stop offset="0.6" stop-color="var(--tile-pink)" stop-opacity="0.35"/>
          <stop offset="1" stop-color="#cfc9c8" stop-opacity="0.5"/>
        </linearGradient>
        <clipPath id="tile-mask">
          <rect x="0" y="0" width="92" height="93" rx="9"/>
          <rect x="97" y="0" width="92" height="93" rx="9"/>
          <rect x="194" y="0" width="92" height="93" rx="9"/>
          <rect x="291" y="0" width="92" height="93" rx="9"/>
          <rect x="0" y="98" width="92" height="93" rx="9"/>
          <rect x="97" y="98" width="92" height="93" rx="9"/>
          <rect x="194" y="98" width="92" height="93" rx="9"/>
          <rect x="291" y="98" width="92" height="93" rx="9"/>
          <rect x="0" y="196" width="92" height="93" rx="9"/>
          <rect x="97" y="196" width="92" height="93" rx="9"/>
          <rect x="194" y="196" width="92" height="93" rx="9"/>
          <rect x="291" y="196" width="92" height="93" rx="9"/>
        </clipPath>
      </defs>
      <g clip-path="url(#tile-mask)">
        <rect width="384" height="290" fill="url(#photo-tone)"/>
        <rect width="384" height="290" fill="url(#photo-shade)"/>
      </g>
    </svg>

    <h2 class="faq-question">What are some of the latest technologies<br>available for improving my oral health?</h2>
    <p class="faq-answer">Dentistry is always evolving and your treatment<br>and safety can be reinforced with new<br>technologies. For example, digital x-rays can<br>greatly reduce your exposure to radiation.<br>Lasers are a non-invasive way to quickly and<br>easily kill bacteria below your gum line. Rapid-<br>align braces can straighten teeth much faster<br>than traditional braces.</p>

    <h2 class="faq-question">How can I get my records transferred to a<br>new dental office?</h2>
    <p class="faq-answer">It’s as simple as asking your former dental<br>office to send the records to the new office.<br>Sometimes you may be requested to sign<br>a release and consent form as well. We are<br>happy to help you with the process.</p>
  </section>

  <section class="panel panel--right">
    <h2 class="faq-question">Is fluoride safe?</h2>
    <p class="faq-answer">The National Oral Health Survey<br>2007-2009 found that 16% of children have<br>mild forms of dental fluorosis that often go<br>unnoticed. Dental fluorosis is a change in the<br>appearance of teeth, often causing small<br>white specks to appear. It is caused when<br>higher than optimal amounts of fluoride are<br>ingested in early childhood.<br>Fluoride-free options for dental care are<br>available at our office.</p>

    <h2 class="faq-question">Are amalgam fillings containing<br>mercury safe?</h2>
    <p class="faq-answer">The Health Board’s official position states that<br>amalgams are safe, but should be avoided<br>in certain people with medical conditions. It<br>is best to consult with your dentist directly.<br>Mercury-free options for dental care are<br>available, and we offer a specific and safe<br>method of mercury removal.</p>

    <h2 class="faq-question">What are dental sealants, and do they<br>contain BPA?</h2>
    <p class="faq-answer">Dental sealants are a way to protect a<br>tooth from forming a cavity by sealing the<br>natural pits and grooves in a tooth with resin.<br>Some sealants do not contain Bis-phenol A,<br>and you may ask your dentist if the type of<br>material used has BPA.</p>

    <h2 class="faq-question">What is gum disease and how can it affect<br>my health?</h2>
    <p class="faq-answer">Gum disease, or periodontal disease, is when<br>bacteria and tartar on your teeth cause<br>inflammation of the gums and the bone<br>supporting your teeth. When severe enough,<br>bone loss occurs, leading to loose teeth and<br>gum abscesses. Gum disease can be treated<br>by daily flossing and regular dental cleaning<br>appointments. Our dentist and dental<br>hygienists will be able to discuss treatment<br>options available for you.</p>
  </section>

</main>
</body>
</html>
```